Consulting, Investors, Joint Venture Website

Founded in April 2018, Marendo Consultants Limited (MCL) is an advisory consulting firm specializing in engaging investors in business ventures in Tanzania.
With extensive experience in construction, energy, oil and gas and the legal professions, our team assembles our expertise that allows foreign investors to set foot and flourish in the Tanzanian market.
MCL is locally owned, founded and registered. Our shareholders are cultured Tanzanian citizens with extensive corporate experience in South Africa, Tanzania, United Kingdom and the United States.

Our mission is to provide responsive and unrivalled professional advice from learned and experienced professionals versed in the local market, with an understanding of the cultural and logistical challenges faced by foreign investors.

Our vision is to provide a complete investor’s package that initiates with company registration, compliance and documentation services and ultimately operational facilitation services.

Target Market(s)

Foreign Investors, International companies

Industry/Entity Type

Business Consultant

Number of Pages Required

5+ page

Requirements
Must have
• It will be 5 pages - Home, About Us, Services, Portfolio, Contact Us
Nice to have
• if it can look like https://www.plorvex.example/
• or https://www.dunetri.example or http://www.quillbrook.example/

```html
<!DOCTYPE html>
<html lang="en">
<head>
<meta charset="utf-8">
<title>Marendo Consultants – Portfolio</title>
<link rel="stylesheet" href="https://fonts.googleapis.com/css2?family=Raleway:wght@400;500;600;700&display=swap">
<style>
  :root {
    --blue: #0d4fa0;
    --blue-deep: #0a3f86;
    --blue-panel: rgba(22, 84, 170, 0.88);
    --orange: #f7931e;
    --white: #ffffff;
    --text-muted: #6b6b6b;
    --line: #f2b36b;
  }
  * { box-sizing: border-box; margin: 0; padding: 0; }
  html, body { width: 745px; height: 1200px; overflow: hidden; }
  body { position: relative; background: var(--white); font-family: "Raleway", sans-serif; color: var(--blue); }
  .abs { position: absolute; }

  /* Hero */
  .hero-photo {
    left: 0; top: 0; width: 745px; height: 344px;
    background: linear-gradient(100deg, #d9b98a 0%, #cfd9e6 30%, #a9c3e2 55%, #c9a69a 80%, #c46c68 100%);
  }
  .hero-veil { left: 0; top: 0; width: 745px; height: 344px; background: linear-gradient(180deg, rgba(255,255,255,0.35), rgba(255,255,255,0.1)); }

  .brand { display: flex; align-items: center; gap: 7px; }
  .header-brand { left: 26px; top: 22px; }
  .brand-mark { width: 22px; height: 22px; background: var(--blue); }
  .brand-name { font-weight: 700; font-size: 17px; letter-spacing: 1.5px; color: var(--blue); }

  .nav a { position: absolute; top: 28px; font-size: 9.5px; color: var(--blue); text-decoration: none; font-weight: 500; white-space: nowrap; }
  .nav a.active { font-weight: 700; }
  .nav a.active::after { content: ""; position: absolute; left: 14px; right: 14px; bottom: -6px; height: 2px; background: var(--orange); }

  .pill { border-radius: 16px; font-size: 10px; font-weight: 500; color: var(--white); display: flex; align-items: center; justify-content: center; text-decoration: none; white-space: nowrap; }
  .pill-orange { background: var(--orange); }
  .pill-blue { background: var(--blue); }
  .header-cta { left: 420px; top: 18px; width: 84px; height: 30px; }

  .header-mail { left: 511px; top: 27px; display: flex; align-items: center; gap: 6px; font-size: 9.5px; font-weight: 600; white-space: nowrap; }
  .social-top { left: 637px; top: 24px; display: flex; gap: 5px; }
  .social-top span { width: 17px; height: 17px; background: var(--blue); display: block; }

  /* Tabs */
  .tabs { left: 26px; top: 208px; width: 693px; height: 44px; background: var(--white); display: flex; }
  .tab { flex: 1; display: flex; align-items: center; justify-content: center; font-size: 11px; font-weight: 500; color: var(--blue); position: relative; }
  .tab.active { background: var(--blue); color: var(--white); }
  .tab.active::after { content: ""; position: absolute; left: 50%; bottom: -13px; margin-left: -11px; border-left: 11px solid transparent; border-right: 11px solid transparent; border-top: 13px solid var(--blue); }

  /* Grid */
  .tile { width: 168px; height: 173px; }
  .tile-refinery { background: linear-gradient(160deg, #1a3f7a 0%, #2f67b0 40%, #b78a52 75%, #16305e 100%); }
  .tile-platform { background: linear-gradient(180deg, #5d9ad8 0%, #a8c8e6 40%, #d8b430 62%, #1f5c94 100%); }
  .tile-sunset { background: linear-gradient(180deg, #e9c56a 0%, #b9c3bd 35%, #7d6b57 65%, #cfc9c0 100%); }
  .tile-offshore { background: linear-gradient(180deg, #9ec1e6 0%, #d5c48e 45%, #c59a2c 62%, #1d4f85 100%); }
  .tile-hover { display: flex; align-items: center; justify-content: center; font-size: 11px; font-weight: 500; color: var(--blue); }
  .tile-hover::before { content: ""; position: absolute; inset: 0; background: rgba(255,255,255,0.72); }
  .tile-hover span { position: relative; }

  .actions { left: 258px; top: 675px; display: flex; gap: 13px; }
  .actions .pill { height: 30px; }

  /* Contact */
  .touch-bg { left: 0; top: 733px; width: 745px; height: 375px; background: linear-gradient(180deg, #5d7fb2 0%, #3f69a8 45%, #2d568f 100%); }
  .touch-title { left: 0; top: 760px; width: 745px; text-align: center; color: var(--white); font-size: 22px; font-weight: 700; }
  .form-card { left: 84px; top: 803px; width: 371px; height: 273px; background: var(--white); }
  .form-title { left: 34px; top: 34px; font-size: 15px; font-weight: 500; color: var(--blue); }
  .form-icon { left: 302px; top: 34px; }
  .field { width: 132px; border-bottom: 1px solid var(--line); font-size: 8px; color: var(--text-muted); padding-bottom: 1px; }
  .send-btn { left: 267px; top: 198px; width: 67px; height: 36px; background: var(--orange); display: flex; align-items: center; justify-content: center; }

  .info-panel { left: 455px; top: 803px; width: 206px; height: 273px; background: var(--blue-panel); color: var(--white); }
  .info-title { left: 32px; top: 34px; font-size: 15px; font-weight: 600; white-space: nowrap; }
  .info-row { left: 28px; display: flex; align-items: flex-start; gap: 12px; font-size: 11px; line-height: 1.2; color: #e8eefa; white-space: nowrap; }
  .info-row svg { flex: none; }
  .info-social { left: 41px; top: 224px; display: flex; gap: 13px; }
  .info-social span { width: 22px; height: 22px; border: 2px solid var(--white); display: block; }

  /* Footer */
  .footer-brand { left: 0; top: 1128px; width: 745px; justify-content: center; }
  .copyright { left: 0; top: 1163px; width: 745px; text-align: center; font-size: 11px; color: var(--blue); }
</style>
</head>
<body>

<header>
  <div class="abs hero-photo" role="img" aria-label="Engineers in hard hats at an offshore rig"></div>
  <div class="abs hero-veil"></div>

  <div class="abs brand header-brand"><span class="brand-mark"></span><span class="brand-name">MARENDO</span></div>

  <nav class="nav">
    <a href="#" style="left:186px">HOME</a>
    <a href="#" style="left:231px">ABOUT US</a>
    <a href="#" style="left:296px">SERVICES</a>
    <a href="#" class="active" style="left:357px">PORTFOLIO</a>
  </nav>
  <a class="abs pill pill-orange header-cta" href="#">CONTACT US</a>

  <div class="abs header-mail">
    <svg width="16" height="11" viewBox="0 0 16 11"><rect x="0.5" y="0.5" width="15" height="10" fill="none" stroke="#0d4fa0"/><path d="M0.5 0.5 L8 6 L15.5 0.5" fill="none" stroke="#0d4fa0"/></svg>
    <span>sample@email.com</span>
  </div>
  <div class="abs social-top" aria-label="Social links"><span></span><span></span><span></span><span></span></div>
</header>

<section>
  <div class="abs tabs">
    <div class="tab active">CATEGORY NAME</div>
    <div class="tab">CATEGORY NAME</div>
    <div class="tab">CATEGORY NAME</div>
    <div class="tab">CATEGORY NAME</div>
  </div>

  <div class="abs tile tile-refinery tile-hover" style="left:26px;top:293px" role="img" aria-label="Refinery at night"><span>PORTFOLIO NAME</span></div>
  <div class="abs tile tile-platform" style="left:201px;top:293px" role="img" aria-label="Offshore platform with yellow bridge"></div>
  <div class="abs tile tile-sunset" style="left:376px;top:293px" role="img" aria-label="Pipeline plant at sunset"></div>
  <div class="abs tile tile-offshore" style="left:551px;top:293px" role="img" aria-label="Offshore oil rig at sea"></div>

  <div class="abs tile tile-refinery" style="left:26px;top:483px" role="img" aria-label="Refinery at night"></div>
  <div class="abs tile tile-platform" style="left:201px;top:483px" role="img" aria-label="Offshore platform with yellow bridge"></div>
  <div class="abs tile tile-sunset tile-hover" style="left:376px;top:483px" role="img" aria-label="Pipeline plant at sunset"><span>PORTFOLIO NAME</span></div>
  <div class="abs tile tile-offshore" style="left:551px;top:483px" role="img" aria-label="Offshore oil rig at sea"></div>

  <div class="abs actions">
    <a class="pill pill-orange" href="#" style="width:85px">CONTACT US</a>
    <a class="pill pill-blue" href="#" style="width:132px">GET AN APPOINTMENT</a>
  </div>
</section>

<section>
  <div class="abs touch-bg" role="img" aria-label="Industrial plant with blue tint"></div>
  <h2 class="abs touch-title">GET IN TOUCH</h2>

  <div class="abs form-card">
    <div class="abs form-title">Send us a message</div>
    <svg class="abs form-icon" width="34" height="22" viewBox="0 0 34 22"><rect x="10" y="1" width="23" height="19" fill="none" stroke="#f7931e" stroke-width="1.5"/><path d="M10 1 L21.5 11 L33 1" fill="none" stroke="#f7931e" stroke-width="1.5"/><path d="M0 6 H7 M2 11 H7 M4 16 H7" stroke="#f7931e" stroke-width="1.5"/></svg>
    <div class="abs field" style="left:36px;top:84px">Enter your name</div>
    <div class="abs field" style="left:202px;top:84px">Enter your email</div>
    <div class="abs field" style="left:36px;top:145px">Enter your subject</div>
    <div class="abs field" style="left:202px;top:145px">Enter your phone number</div>
    <div class="abs field" style="left:36px;top:206px">Enter your message</div>
    <div class="abs send-btn"><svg width="24" height="20" viewBox="0 0 24 20"><path d="M1 9 L23 1 L16 19 L11 11 Z M11 11 L23 1" fill="none" stroke="#fff" stroke-width="1.5" stroke-linejoin="round"/></svg></div>
  </div>

  <div class="abs info-panel">
    <div class="abs info-title">Contact Information</div>
    <div class="abs info-row" style="top:80px">
      <svg width="28" height="28" viewBox="0 0 28 28"><path d="M14 23 C9 16 7 13 7 10 a7 7 0 0 1 14 0 c0 3 -2 6 -7 13 Z" fill="none" stroke="#fff" stroke-width="1.3"/><circle cx="14" cy="10" r="2.5" fill="none" stroke="#fff" stroke-width="1.3"/><path d="M3 27 L8 19 M25 27 L20 19 M3 27 H25" stroke="#fff" stroke-width="1.3"/></svg>
      <span>1234 Sample Address<br>Sample city</span>
    </div>
    <div class="abs info-row" style="top:128px">
      <svg width="28" height="26" viewBox="0 0 28 26"><path d="M1 10 L14 1 L27 10 V25 H1 Z" fill="none" stroke="#fff" stroke-width="1.3"/><path d="M1 10 L14 19 L27 10" fill="none" stroke="#fff" stroke-width="1.3"/><circle cx="14" cy="9" r="3" fill="none" stroke="#fff" stroke-width="1.1"/></svg>
      <span style="padding-top:5px">sample@email.com</span>
    </div>
    <div class="abs info-row" style="top:175px">
      <svg width="28" height="28" viewBox="0 0 28 28"><path d="M6 2 L10 8 L7 11 C9 16 12 19 17 21 L20 18 L26 22 L23 26 C12 25 3 16 2 5 Z" fill="none" stroke="#fff" stroke-width="1.3" stroke-linejoin="round"/></svg>
      <span style="padding-top:8px">12345-567-34343</span>
    </div>
    <div class="abs info-social" aria-label="Social links"><span></span><span></span><span></span><span></span></div>
  </div>
</section>

<footer>
  <div class="abs brand footer-brand"><span class="brand-mark"></span><span class="brand-name">MARENDO</span></div>
  <p class="abs copyright">Copyright © 218 - Marendo Consultant</p>
</footer>

</body>
</html>
```